Web design for insurance consultant. Target clients are (re)insurers, insurtech firms and vendor...

Need a crisp, modern website which will talk briefly about the firm and its principal founder. And, details around services offered for 3 different target clients: (1) re/insurance companies, (2) insurtech and IoT firms, and (3) vendors such as claims adjusting firms and home inspection firms supporting insurers

Target Market(s)

C-suite leaders of insurance companies, reinsurance companies, insurtech firms looking to innovate property insurance, and vendors selling to these insurance companies. Focus is property insurance in coastal, catastrophe-exposed regions of the US.

Coding

Coded - Design and coding required

Number of Pages Required

5+ page

Other font styles liked:
• not sure of font wanted - classic, but modern

Colors
0792cd
00a990

Requirements
Must have
• First box should use the attached "light bulb storm" picture as background.
• one change overall - remove "Get a quote" button - we do not sell to consumers, it's strictly B2B.
• For the 3 segments, use the pictures below. I could not find one I liked for "TPAs/Vendors", so welcome your suggestions.
• Want quotes in the boxes of each of the 3 market segments.
• Button on each of the 3 market segments would lead to content (not yet finished) that will explain in more detail the services to be provided to them.
Should not have
• don't want velkori plots or others showing location of business (waste of space, in my opinion)

```html
<!DOCTYPE html>
<html lang="en">
<head>
<meta charset="utf-8">
<title>Halvern Consulting</title>
<link rel="stylesheet" href="https://fonts.googleapis.com/css2?family=Raleway:wght@300;400;500;600;700;800&family=Open+Sans:wght@400;600&display=swap">
<style>
:root{
  --navy:#0c4f8b;
  --navy-deep:#0a3f70;
  --green:#6a9a0f;
  --green-light:#7fae1c;
  --ink:#2a2a2a;
  --muted:#777;
  --line:#d8d8d8;
  --grey-band:#efefef;
  --white:#fff;
}
*{box-sizing:border-box;margin:0;padding:0}
html,body{width:1200px;height:4196px;overflow:hidden}
body{font-family:"Open Sans",Arial,sans-serif;color:var(--ink);background:var(--white);position:relative}
section,header,footer,.top-bar{position:absolute;left:0;width:1200px}
.abs{position:absolute}
.heading{font-family:"Raleway",Arial,sans-serif}
.btn{position:absolute;background:var(--green);color:var(--white);font-family:"Raleway",Arial,sans-serif;font-size:20px;text-transform:uppercase;display:flex;align-items:center;justify-content:center;letter-spacing:.5px}

/* top bar */
.top-bar{top:0;height:40px;background:var(--navy)}
.top-contact{position:absolute;top:0;height:40px;display:flex;align-items:center;gap:10px;color:var(--white);font-size:15px}
.top-icon{width:26px;height:26px;border-radius:50%;background:var(--green);display:flex;align-items:center;justify-content:center}

/* header */
.site-header{top:40px;height:90px;background:var(--white)}
.brand{position:absolute;left:78px;top:22px;display:flex;align-items:center;gap:12px}
.brand-mark{width:48px;height:48px;border-radius:50%;background:var(--navy)}
.brand-name{font-family:"Raleway",Arial,sans-serif;font-weight:700;font-size:28px;color:var(--navy)}
.main-nav{position:absolute;right:78px;top:0;height:90px;display:flex;align-items:center;gap:38px;font-family:"Raleway",Arial,sans-serif;font-size:16px;color:#333;text-transform:uppercase}
.main-nav .active{color:var(--green);border-bottom:2px solid var(--green);padding-bottom:4px}

/* hero */
.hero{top:130px;height:550px;background:linear-gradient(90deg,#c9c3bd 0%,#d9d6d2 35%,#eef0f2 60%,#f4f6f8 100%)}
.hero-photo{position:absolute;left:0;top:0;width:760px;height:550px;background:linear-gradient(120deg,#a9a097 0%,#cfc8bf 45%,rgba(238,240,242,0) 100%)}
.hero-title-light{position:absolute;right:78px;top:140px;font-family:"Raleway",Arial,sans-serif;font-weight:300;font-size:68px;color:var(--navy);letter-spacing:2px}
.hero-title-bold{position:absolute;right:78px;top:210px;font-family:"Raleway",Arial,sans-serif;font-weight:800;font-size:68px;color:var(--navy);letter-spacing:1px}
.hero-lede{position:absolute;right:78px;top:300px;font-size:16px;color:#333}
.hero-arrow{position:absolute;right:20px;top:240px}

/* subscribe */
.subscribe{top:680px;height:103px;background:var(--navy)}
.sub-label{position:absolute;left:104px;top:26px;display:flex;align-items:center;gap:16px;color:var(--white);font-family:"Raleway",Arial,sans-serif;font-size:27px}
.sub-icon{width:50px;height:50px;border-radius:50%;background:var(--white);display:flex;align-items:center;justify-content:center}
.sub-input{position:absolute;left:515px;top:25px;width:377px;height:52px;background:var(--white);font-size:14px;color:#555;padding:0 18px;display:flex;align-items:center}

/* about */
.about{top:783px;height:694px;background:var(--white)}
.eyebrow{position:absolute;width:1200px;text-align:center;color:var(--green);font-family:"Raleway",Arial,sans-serif;font-size:22px;letter-spacing:1px}
.section-title{position:absolute;width:1200px;text-align:center;color:var(--navy);font-family:"Raleway",Arial,sans-serif;font-weight:700;font-size:42px}
.about-heading{position:absolute;left:283px;top:180px;font-family:"Raleway",Arial,sans-serif;font-weight:600;font-size:32px;color:#222}
.about-text{position:absolute;left:283px;top:228px;width:325px;font-size:13.5px;line-height:26px;color:var(--muted)}
.about-photo{position:absolute;left:635px;top:187px;width:302px;height:330px;background:linear-gradient(180deg,#d6dde2 0%,#9aa6b1 55%,#2b3442 100%)}
.call-label{position:absolute;left:283px;top:562px;color:var(--green);font-family:"Raleway",Arial,sans-serif;font-weight:700;font-size:21px}
.call-number{position:absolute;left:283px;top:592px;color:var(--navy);font-family:"Raleway",Arial,sans-serif;font-weight:600;font-size:33px}

/* services */
.services{top:1477px;height:615px;background:var(--grey-band)}
.services-intro{position:absolute;left:290px;top:112px;width:620px;text-align:center;font-size:13.5px;line-height:24px;color:var(--muted)}
.service{position:absolute;top:200px;width:320px;text-align:center}
.service-icon{width:130px;height:130px;margin:0 auto;border-radius:50%;border:6px solid var(--navy);background:var(--white);display:flex;align-items:center;justify-content:center}
.service-title{margin-top:26px;font-family:"Raleway",Arial,sans-serif;font-weight:700;font-size:23px;color:var(--navy)}
.service-quote{margin:16px auto 0;width:270px;font-size:13.5px;line-height:24px;color:var(--muted)}
.service .btn{position:relative;margin:22px auto 0;width:157px;height:46px;font-size:17px}

/* news */
.news{top:2092px;height:559px;background:var(--white)}
.news-card{position:absolute;top:145px;width:333px}
.news-photo{width:333px;height:252px;position:relative;background:linear-gradient(160deg,#5a6573 0%,#2c3542 60%,#1c2330 100%)}
.news-day{position:absolute;left:0;top:0;width:60px;height:48px;background:var(--green);color:var(--white);font-family:"Raleway",Arial,sans-serif;font-weight:700;font-size:32px;display:flex;align-items:center;justify-content:center}
.news-month{position:absolute;left:0;top:48px;width:60px;height:30px;background:var(--navy);color:var(--white);font-size:15px;display:flex;align-items:center;justify-content:center}
.news-title{margin-top:20px;padding-right:40px;font-family:"Raleway",Arial,sans-serif;font-weight:600;font-size:17px;line-height:30px;color:#222;position:relative}
.news-plus{position:absolute;right:6px;top:12px;font-size:30px;font-weight:300;color:var(--green)}
.news-rule{margin-top:16px;height:4px;background:var(--line)}

/* testimonials */
.testimonials{top:2651px;height:571px;background:linear-gradient(90deg,#e4edf3 0%,#dce7ef 50%,#c9d4dc 100%)}
.testimonial-scene{position:absolute;right:0;top:0;width:520px;height:571px;background:linear-gradient(200deg,#e2e8ec 0%,#b8a78c 55%,#8d7a60 100%)}
.testimonial-card{position:absolute;left:210px;top:196px;width:780px;height:230px;background:rgba(255,255,255,.95)}
.client-photo{position:absolute;left:12px;top:9px;width:165px;height:210px;background:linear-gradient(180deg,#d7cfc7 0%,#b59d85 60%,#8e7663 100%)}
.quote-badge{position:absolute;left:232px;top:26px;width:36px;height:36px;border-radius:50%;background:var(--green)}
.quote-text{position:absolute;left:285px;top:22px;width:470px;font-size:14px;line-height:30px;color:#444}
.client-name{position:absolute;right:30px;bottom:18px;display:flex;align-items:center;gap:12px;font-family:"Raleway",Arial,sans-serif;font-weight:700;font-size:18px;color:var(--navy)}
.client-name span{display:block;width:26px;height:4px;background:var(--navy)}
.dots{position:absolute;left:540px;top:484px;display:flex;gap:10px}
.dot{width:16px;height:16px;border-radius:50%;background:var(--white);border:2px solid #cfd8de}
.dot.on{background:var(--green);border-color:var(--green)}

/* contact */
.contact{top:3222px;height:615px;background:var(--white)}
.contact-sub{position:absolute;width:1200px;top:110px;text-align:center;font-size:15px;color:#444}
.contact-sub b{color:var(--navy)}
.field{position:absolute;left:313px;width:574px;border:2px solid #ededed;font-size:14px;color:#666;padding:0 18px;display:flex;align-items:center;justify-content:space-between}
.field.focus{border-color:var(--green)}

/* footer */
.site-footer{top:3837px;height:359px;background:linear-gradient(180deg,#125a98 0%,#0c4f8b 100%)}
.footer-mark{position:absolute;left:548px;top:46px;width:104px;height:104px;border-radius:50%;background:var(--white)}
.footer-name{position:absolute;width:1200px;top:160px;text-align:center;font-family:"Raleway",Arial,sans-serif;font-weight:700;font-size:18px;color:var(--white)}
.socials{position:absolute;left:530px;top:180px;display:flex;gap:12px}
.social{width:40px;height:40px;border-radius:50%;background:#1d8fd6}
.footer-links{position:absolute;width:1200px;top:240px;text-align:center;font-size:14px;color:var(--white)}
.footer-links span{margin:0 8px}
.copyright{position:absolute;width:1200px;top:266px;text-align:center;font-size:14px;color:var(--white)}
</style>
</head>
<body>

<div class="top-bar">
  <div class="top-contact" style="left:760px">
    <div class="top-icon"><svg width="14" height="14" viewBox="0 0 24 24"><path fill="#fff" d="M6.6 10.8a15 15 0 0 0 6.6 6.6l2.2-2.2c.3-.3.7-.4 1-.2 1.1.4 2.3.6 3.6.6.6 0 1 .4 1 1V20c0 .6-.4 1-1 1A17 17 0 0 1 3 4c0-.6.4-1 1-1h3.5c.6 0 1 .4 1 1 0 1.3.2 2.5.6 3.6.1.3 0 .7-.2 1z"/></svg></div>
    123 456 7890
  </div>
  <div class="top-contact" style="left:910px">
    <div class="top-icon"><svg width="14" height="14" viewBox="0 0 24 24"><path fill="#fff" d="M3 5h18v14H3z"/><path fill="none" stroke="#6a9a0f" stroke-width="2" d="M3 5l9 8 9-8"/></svg></div>
    info@halvernconsulting.com
  </div>
</div>

<header class="site-header">
  <div class="brand"><div class="brand-mark"></div><div class="brand-name">Halvern</div></div>
  <nav class="main-nav">
    <span class="active">Home</span><span>About</span><span>Services</span><span>News</span><span>Contact</span>
    <svg width="18" height="18" viewBox="0 0 24 24"><circle cx="10" cy="10" r="6.5" fill="none" stroke="#555" stroke-width="2"/><path d="M15 15l6 6" stroke="#555" stroke-width="2"/></svg>
  </nav>
</header>

<section class="hero">
  <div class="hero-photo" role="img" aria-label="Two consultants working together at a laptop in a bright office"></div>
  <div class="hero-title-light">HALVERN</div>
  <div class="hero-title-bold">CONSULTING</div>
  <div class="hero-lede">Lorem Ipsum simple text of print and typesetting industry of print text</div>
  <div class="btn" style="right:78px;top:345px;width:171px;height:48px">Contact Us</div>
  <svg class="hero-arrow" width="20" height="30" viewBox="0 0 20 30"><path d="M5 4l10 11-10 11" fill="none" stroke="#555" stroke-width="2"/></svg>
</section>

<section class="subscribe">
  <div class="sub-label">
    <div class="sub-icon"><svg width="24" height="24" viewBox="0 0 24 24"><path fill="#6a9a0f" d="M3 5h18v14H3z"/><path fill="none" stroke="#fff" stroke-width="2" d="M3 5l9 8 9-8"/></svg></div>
    Stay In Touch With Updates!
  </div>
  <div class="sub-input">Enter Email *</div>
  <div class="btn" style="left:900px;top:25px;width:168px;height:52px;font-size:21px">Subscribe</div>
</section>

<section class="about">
  <div class="eyebrow" style="top:50px">WELCOME TO</div>
  <div class="section-title" style="top:88px">HALVERN CONSULTING</div>
  <div class="about-heading">About Us</div>
  <p class="about-text">Lorem Ipsum is simply dummy text of the printing and typesetting industry. Lorem Ipsum has been the industry's standard dummy text ever since the 1500s, when an unknown printer. Lorem Ipsum is simply dummy text of the printing and typesetting industry. Lorem Ipsum has been the industry's standard dummy text ever since the 1500s, when an unknown printer.</p>
  <div class="about-photo" role="img" aria-label="Portrait of the principal founder in a dark business suit"></div>
  <div class="btn" style="left:285px;top:462px;width:168px;height:50px">Learn More</div>
  <div class="call-label">Call Us On :</div>
  <div class="call-number">(123) 456 7890</div>
</section>

<section class="services">
  <div class="section-title" style="top:52px">SERVICES WE PROVIDE</div>
  <p class="services-intro">Lorem Ipsum is simply dummy text of the printing and typesetting industry. Lorem Ipsum has been the industry's standard dummy text when an unknown</p>

  <div class="service" style="left:97px">
    <div class="service-icon"><svg width="70" height="70" viewBox="0 0 70 70" fill="none" stroke="#0c4f8b" stroke-width="3"><path d="M10 30a25 18 0 0 1 50 0z"/><path d="M35 30v28a5 5 0 0 1-10 0"/></svg></div>
    <div class="service-title">(Re)Insurers</div>
    <p class="service-quote">"Halvern has a unique skill set in property cat that helped us refine our approach, particularly in the challenging markets."</p>
    <div class="btn">Learn More</div>
  </div>

  <div class="service" style="left:439px">
    <div class="service-icon"><svg width="70" height="70" viewBox="0 0 70 70" fill="none" stroke="#0c4f8b" stroke-width="3"><circle cx="35" cy="35" r="10"/><circle cx="35" cy="8" r="5"/><circle cx="35" cy="62" r="5"/><circle cx="8" cy="35" r="5"/><circle cx="62" cy="35" r="5"/><path d="M35 13v12M35 45v12M13 35h12M45 35h12"/></svg></div>
    <div class="service-title">Insurtech / IoT</div>
    <p class="service-quote">""We didn't realize how hard insurance is. Tovan's operational insights and supply-side views helped."</p>
    <div class="btn">Learn More</div>
  </div>

  <div class="service" style="left:785px">
    <div class="service-icon"><svg width="70" height="70" viewBox="0 0 70 70" fill="none" stroke="#0c4f8b" stroke-width="3"><circle cx="35" cy="22" r="11"/><path d="M14 62c0-14 9-22 21-22s21 8 21 22z"/><path d="M35 40l-4 8 4 12 4-12z"/></svg></div>
    <div class="service-title">Vendors &amp; TPAs</div>
    <p class="service-quote">"Halvern knows everybody in this space. As important as his connections were to us, he also provided huge value."</p>
    <div class="btn">Learn More</div>
  </div>
</section>

<section class="news">
  <div class="section-title" style="top:56px">LATEST NEWS</div>

  <article class="news-card" style="left:78px">
    <div class="news-photo" role="img" aria-label="Team of colleagues in a meeting room">
      <div class="news-day">02</div><div class="news-month">April</div>
    </div>
    <div class="news-title">Lorem Ipsum is simply text of the printing &amp; type.<span class="news-plus">+</span></div>
    <div class="news-rule"></div>
  </article>

  <article class="news-card" style="left:434px">
    <div class="news-photo" role="img" aria-label="Two professionals discussing across a desk" style="background:linear-gradient(160deg,#7a6a5c 0%,#4a3f36 60%,#2c241f 100%)">
      <div class="news-day">01</div><div class="news-month">April</div>
    </div>
    <div class="news-title">Lorem Ipsum is simply text of the printing &amp; type.<span class="news-plus">+</span></div>
    <div class="news-rule"></div>
  </article>

  <article class="news-card" style="left:789px">
    <div class="news-photo" role="img" aria-label="Business people reviewing documents at a table" style="background:linear-gradient(160deg,#b9bcc0 0%,#6e7378 55%,#34383d 100%)">
      <div class="news-day">01</div><div class="news-month">April</div>
    </div>
    <div class="news-title">Lorem Ipsum is simply text of the printing &amp; type.<span class="news-plus">+</span></div>
    <div class="news-rule"></div>
  </article>
</section>

<section class="testimonials">
  <div class="testimonial-scene" role="img" aria-label="Relaxed client leaning back in a wicker chair"></div>
  <div class="eyebrow" style="top:70px">TESTIMONIALS</div>
  <div class="section-title" style="top:108px">WHAT OUR CLIENT SAY</div>
  <div class="testimonial-card">
    <div class="client-photo" role="img" aria-label="Client portrait"></div>
    <div class="quote-badge"></div>
    <p class="quote-text">" Lorem Ipsum is simply dummy text of the printing and typesetting industry. Lorem Ipsum has been the industry's standard dummy text ever since the 1500s, when an unknown printer took a galley of type and scrambled it to make a type specimen book it has survived no. "</p>
    <div class="client-name"><span></span>CLIENT NAME</div>
  </div>
  <div class="dots"><div class="dot"></div><div class="dot"></div><div class="dot on"></div><div class="dot"></div></div>
</section>

<section class="contact">
  <div class="section-title" style="top:55px">CONTACT US</div>
  <p class="contact-sub">If you need an have any question for Contact us Today On <b>123 456 7890</b></p>
  <div class="field focus" style="top:168px;height:48px">Name *<svg width="16" height="16" viewBox="0 0 24 24" fill="none" stroke="#bbb" stroke-width="2"><circle cx="12" cy="8" r="4"/><path d="M4 21c0-5 4-7 8-7s8 2 8 7"/></svg></div>
  <div class="field" style="top:232px;height:48px">Email *<svg width="16" height="16" viewBox="0 0 24 24" fill="none" stroke="#bbb" stroke-width="2"><path d="M3 6h18v12H3z"/><path d="M3 6l9 7 9-7"/></svg></div>
  <div class="field" style="top:296px;height:48px">Phone *<svg width="16" height="16" viewBox="0 0 24 24" fill="none" stroke="#bbb" stroke-width="2"><path d="M6.6 10.8a15 15 0 0 0 6.6 6.6l2.2-2.2 4.6 1V20A17 17 0 0 1 3 4h4.2l1 4.6z"/></svg></div>
  <div class="field" style="top:362px;height:124px;align-items:flex-start;padding-top:14px">Message *<svg width="16" height="16" viewBox="0 0 24 24" fill="none" stroke="#bbb" stroke-width="2"><path d="M4 5h16v11H9l-5 4z"/></svg></div>
  <div class="btn" style="left:523px;top:501px;width:154px;height:50px;font-size:21px">Submit</div>
</section>

<footer class="site-footer">
  <div class="footer-mark"></div>
  <div class="footer-name">Halvern</div>
  <div class="socials"><div class="social"></div><div class="social"></div><div class="social"></div></div>
  <div class="footer-links"><span>Home</span>|<span>About Us</span>|<span>Services</span>|<span>News</span>|<span>Contact Us</span></div>
  <div class="copyright">©Halvern consulting -2019 All Rights Reserved.</div>
</footer>

</body>
</html>
```